Exciting & Elegant Stationary Pack

Stationary consists of
1. Letter head / Envelope
2. Business Card
3. Invoice
4. 40x40mm sticker

Attached files;

1. Logo (Other formats available on request)
2. MS word Doc - For information and description of design
3. Website image (This will be our new website so use the colours so everything ties together)
4. Sample of stationary pack we like, but feel free to be creative

Target Market(s)

Home improvement

Industry/Entity Type

Construction

Other font styles liked:
• Leave up to designer - We like font used on (website attached image)

Requirements
Must have
• Please look at uploaded file of sample website and use colours
Nice to have
• Any type of business card design - eg. metal, die cut, embossed, etc...

```html
<!DOCTYPE html>
<html lang="en">
<head>
<meta charset="utf-8">
<title>Laymark Tiling — Stationery</title>
<link href="https://fonts.googleapis.com/css2?family=Montserrat:ital,wght@0,400;0,500;0,600;0,700;0,800;1,600;1,700&display=swap" rel="stylesheet">
<style>
  :root {
    --navy: #1c4a73;
    --navy-deep: #163d61;
    --mist: #c8d5e0;
    --ink: #222a33;
    --rule: #8a9099;
    --paper: #ffffff;
    --stage-light: #ddd0b8;
    --stage-dark: #1b1b1d;
  }
  * { box-sizing: border-box; margin: 0; padding: 0; }
  html, body { width: 1200px; height: 2250px; overflow: hidden; }
  body { font-family: "Montserrat", Arial, sans-serif; color: var(--ink); position: relative; }

  .stage { position: absolute; left: 0; width: 1200px; }
  .stage--invoice { top: 0; height: 1330px; background: var(--stage-light); }
  .stage--cards { top: 1330px; height: 920px; background: var(--stage-dark); }

  .sheet { position: absolute; background: var(--paper); overflow: hidden; }
  .sheet * { position: absolute; }

  /* Invoice */
  .invoice { left: 210px; top: 115px; width: 780px; height: 1100px; }
  .invoice .corner-tab { right: 0; top: 80px; width: 46px; height: 40px; background: var(--navy); }
  .invoice .brand { left: 50px; top: 140px; font-size: 26px; font-weight: 800; color: var(--navy); letter-spacing: 1px; }
  .invoice .brand-band { left: 0; top: 200px; width: 232px; height: 34px; background: var(--navy); }
  .invoice .brand-band-tail { left: 244px; top: 200px; width: 60px; height: 34px; background: var(--navy); }
  .invoice .contact { left: 380px; top: 92px; font-size: 13px; font-weight: 600; color: var(--navy); line-height: 19px; }
  .rule { height: 1px; background: var(--rule); }
  .invoice .rule--head { left: 380px; top: 168px; width: 360px; }
  .invoice .rule--client { left: 60px; top: 252px; width: 360px; }
  .invoice .rule--table { left: 60px; top: 340px; width: 680px; }
  .invoice .rule--rows { left: 60px; top: 410px; width: 680px; }
  .invoice .rule--foot { left: 60px; top: 880px; width: 500px; }

  .total-box { background: var(--navy); color: #fff; }
  .invoice .total-box--top { left: 430px; top: 186px; width: 310px; height: 124px; }
  .total-box .label { font-size: 13px; font-weight: 700; letter-spacing: .5px; }
  .total-box--top .label { left: 20px; top: 30px; }
  .total-box--top .amount { right: 20px; top: 50px; font-size: 30px; font-weight: 700; }
  .invoice .total-box--foot { left: 560px; top: 840px; width: 180px; height: 64px; text-align: right; }
  .total-box--foot .label { right: 18px; top: 11px; }
  .total-box--foot .amount { right: 18px; top: 28px; font-size: 20px; font-weight: 700; }

  .invoice .client { left: 60px; top: 268px; font-size: 13px; font-weight: 600; line-height: 18px; }
  .invoice .date { right: 40px; top: 318px; font-size: 11px; font-weight: 500; }

  .th { font-size: 12px; font-weight: 600; color: var(--navy); }
  .td { font-size: 10px; font-weight: 500; }
  .invoice .th--rate { left: 430px; top: 360px; }
  .invoice .th--unit { left: 560px; top: 360px; }
  .invoice .th--total { left: 690px; top: 350px; }
  .invoice .invoice-number { left: 60px; top: 385px; font-size: 12px; font-weight: 500; }
  .invoice .td--rate { left: 430px; top: 390px; }
  .invoice .td--unit { left: 565px; top: 382px; }
  .invoice .td--total { left: 680px; top: 372px; }
  .invoice .th--desc { left: 90px; top: 432px; }
  .invoice .td--desc { left: 90px; top: 455px; }

  .invoice .brand-faint { left: 560px; top: 930px; font-size: 22px; font-weight: 800; color: var(--mist); letter-spacing: 1px; }
  .invoice .payment { left: 60px; top: 930px; width: 400px; height: 78px; border: 1px solid var(--rule); padding: 12px 12px; font-size: 12px; font-weight: 500; line-height: 17px; position: absolute; }
  .invoice .thanks { left: 0; width: 780px; top: 1040px; text-align: center; font-size: 13px; font-weight: 700; color: var(--navy); letter-spacing: .5px; }

  /* Business cards */
  .card { top: 1650px; width: 540px; height: 310px; }
  .card--front { left: 30px; }
  .card--back { left: 630px; }

  .card--front .tab { left: 0; top: 40px; width: 22px; height: 42px; background: var(--navy); }
  .card--front .name { left: 40px; top: 36px; font-size: 22px; font-weight: 700; font-style: italic; color: var(--navy); }
  .card--front .role { left: 40px; top: 66px; font-size: 13px; font-weight: 600; font-style: italic; color: var(--navy); }
  .card--front .head-rule { left: 270px; top: 64px; width: 270px; height: 3px; background: var(--navy); }
  .card--front .head-name { right: 20px; top: 38px; font-size: 17px; font-weight: 800; color: var(--navy); letter-spacing: .5px; }
  .card--front .details { left: 30px; top: 126px; list-style: none; }
  .details li { position: relative; display: block; height: 30px; font-size: 14px; font-weight: 600; color: var(--navy); padding-left: 30px; line-height: 20px; }
  .details .ico { left: 0; top: 1px; width: 19px; height: 18px; background: var(--navy); border-radius: 3px; }
  .details .ico svg { position: absolute; left: 3px; top: 2px; }
  .card--front .brand-block { right: 30px; bottom: 40px; display: flex; align-items: center; gap: 10px; position: absolute; }
  .brand-block .mark { width: 20px; height: 20px; background: var(--navy); position: static; }
  .brand-block .word { position: static; font-size: 24px; font-weight: 800; color: var(--navy); letter-spacing: 1px; }

  .card--back .band { left: 0; bottom: 0; width: 540px; height: 70px; background: var(--navy); }
  .card--back .brand-block { left: 0; width: 540px; top: 105px; display: flex; justify-content: center; align-items: center; gap: 12px; }
  .card--back .brand-block .word { font-size: 32px; }
  .card--back .brand-block .mark { width: 26px; height: 26px; }
</style>
</head>
<body>

<section class="stage stage--invoice">
  <article class="sheet invoice">
    <div class="corner-tab"></div>
    <div class="brand">LAYMARK TILING</div>
    <div class="brand-band"></div>
    <div class="brand-band-tail"></div>

    <div class="contact">
      A : PO BOX 48 HARBOUR HEIGHTS NSW 2100<br>
      W : WWW.LAYMARKTILING.COM.AU<br>
      M : 0400 318 572
    </div>
    <div class="rule rule--head"></div>

    <div class="total-box total-box--top">
      <span class="label">TOTAL</span>
      <span class="amount">$7,500.00</span>
    </div>
    <div class="rule rule--client"></div>

    <div class="client">To<br>NORTHVALE DEVELOPMENTS<br>ADDRESS :<br>KESTREL RD WESTMEAD</div>
    <div class="date">Date : 11/08/2016</div>
    <div class="rule rule--table"></div>

    <span class="th th--rate">Rate</span>
    <span class="th th--unit">Unit</span>
    <span class="th th--total">Total</span>
    <span class="invoice-number">INVOICE &nbsp;Number : 30413283</span>
    <span class="td td--rate">$3750.00</span>
    <span class="td td--unit">02</span>
    <span class="td td--total">$7,500.00</span>
    <div class="rule rule--rows"></div>
    <span class="th th--desc">Description</span>
    <span class="td td--desc">Services , Design</span>

    <div class="rule rule--foot"></div>
    <div class="total-box total-box--foot">
      <span class="label">TOTAL</span>
      <span class="amount">$7,500.0</span>
    </div>
    <div class="brand-faint">LAYMARK TILING</div>

    <div class="payment">
      Payment Methods<br>
      Online wallet : pay@laymarktiling.com.au<br>
      we accept all major cards, bank transfer
    </div>
    <div class="thanks">THANK YOU FOR &nbsp;YOUR BUSINESS</div>
  </article>
</section>

<section class="stage stage--cards"></section>

<article class="sheet card card--front">
  <div class="tab"></div>
  <div class="name">Dana Loring</div>
  <div class="role">Project Manager</div>
  <div class="head-rule"></div>
  <div class="head-name">LAYMARK TILING</div>
  <ul class="details">
    <li><span class="ico"><svg width="13" height="14" viewBox="0 0 13 14"><rect x="3" y="1" width="7" height="12" rx="1.5" fill="none" stroke="#fff" stroke-width="1.4"/><circle cx="6.5" cy="10.5" r=".9" fill="#fff"/></svg></span>0400 318 572</li>
    <li><span class="ico"><svg width="13" height="14" viewBox="0 0 13 14"><circle cx="6.5" cy="7" r="5" fill="none" stroke="#fff" stroke-width="1.3"/><path d="M1.5 7h10M6.5 2c-2.5 3-2.5 7 0 10M6.5 2c2.5 3 2.5 7 0 10" fill="none" stroke="#fff" stroke-width="1"/></svg></span>www.laymarktiling.com.au</li>
    <li><span class="ico"><svg width="13" height="14" viewBox="0 0 13 14"><rect x="1.5" y="3.5" width="10" height="7" fill="none" stroke="#fff" stroke-width="1.3"/><path d="M1.5 3.5l5 4 5-4" fill="none" stroke="#fff" stroke-width="1.1"/></svg></span>info@laymarktiling.com.au</li>
    <li>L : 204519c</li>
  </ul>
  <div class="brand-block"><span class="mark"></span><span class="word">LAYMARK TILING</span></div>
</article>

<article class="sheet card card--back">
  <div class="brand-block"><span class="mark"></span><span class="word">LAYMARK TILING</span></div>
  <div class="band"></div>
</article>

</body>
</html>
```